Kelvor Plant Services

We are a heavy diesel mechanical business with additional air con certificates, remapping engine rebuilt

Contact Information for Business Card

Company Name, Director Name, Managing Director, Contact details, email and website

Font styles to use
Serif
Script

```html
<!DOCTYPE html>
<html lang="en">
<head>
<meta charset="utf-8">
<title>Kelvor Plant Services – Business Card</title>
<link rel="stylesheet" href="https://fonts.googleapis.com/css2?family=Open+Sans:wght@400;600;700&display=swap">
<style>
  :root {
    --navy: #262a80;
    --navy-deep: #1d2068;
    --ink: #2b2b2b;
    --charcoal: #1e1e1e;
    --paper: #ffffff;
    --stage: #2a2c30;
    --muted: #555555;
  }
  * { margin: 0; padding: 0; box-sizing: border-box; }
  html, body { width: 1200px; height: 900px; overflow: hidden; }
  body {
    background: var(--stage);
    font-family: "Open Sans", Arial, sans-serif;
    position: relative;
  }
  .card {
    position: absolute;
    left: 285px;
    width: 630px;
    height: 360px;
    border-radius: 22px;
    overflow: hidden;
  }
  .card--front { top: 60px; background: var(--paper); }
  .card--back {
    top: 480px;
    background: var(--navy);
    display: flex;
    align-items: center;
    justify-content: center;
  }
  .corner-band { position: absolute; left: 0; bottom: 0; }
  .holder { position: absolute; left: 46px; top: 44px; }
  .holder__name {
    font-weight: 700;
    font-size: 27px;
    color: var(--navy);
    letter-spacing: -0.5px;
  }
  .holder__role { font-size: 14px; color: var(--muted); margin-top: 2px; }
  .contacts { position: absolute; left: 30px; top: 128px; list-style: none; }
  .contacts li {
    display: flex;
    align-items: center;
    gap: 9px;
    font-size: 16px;
    color: var(--ink);
    line-height: 26px;
  }
  .contacts svg { width: 12px; height: 12px; fill: var(--navy); }
  .divider {
    position: absolute;
    left: 150px;
    right: 40px;
    top: 232px;
    height: 1.5px;
    background: var(--navy);
  }
  .brand {
    display: flex;
    align-items: center;
    gap: 10px;
    font-weight: 700;
    color: var(--navy);
  }
  .brand__dot {
    width: 16px; height: 16px;
    border-radius: 50%;
    background: currentColor;
  }
  .card--front .brand {
    position: absolute;
    right: 44px;
    top: 150px;
    font-size: 26px;
  }
  .card--back .brand { color: var(--paper); font-size: 36px; }
  .card--back .brand__dot { width: 22px; height: 22px; }
  .address {
    position: absolute;
    right: 44px;
    top: 254px;
    text-align: right;
    font-size: 17px;
    font-style: normal;
    color: var(--ink);
    line-height: 26px;
  }
</style>
</head>
<body>
  <section class="card card--front" aria-label="Business card front">
    <svg class="corner-band" width="170" height="70" viewBox="0 0 170 70" aria-hidden="true">
      <polygon points="0,30 120,30 150,70 0,70" fill="var(--charcoal)"/>
      <polygon points="0,18 110,18 120,30 0,30" fill="var(--navy)"/>
    </svg>

    <div class="holder">
      <p class="holder__name">DORIAN WELCH</p>
      <p class="holder__role">Managing Director</p>
    </div>

    <ul class="contacts">
      <li>
        <svg viewBox="0 0 24 24"><path d="M6.6 10.8a15 15 0 0 0 6.6 6.6l2.2-2.2a1 1 0 0 1 1-.25 11.4 11.4 0 0 0 3.6.57 1 1 0 0 1 1 1V20a1 1 0 0 1-1 1A17 17 0 0 1 3 4a1 1 0 0 1 1-1h3.5a1 1 0 0 1 1 1c0 1.25.2 2.45.57 3.57a1 1 0 0 1-.25 1z"/></svg>
        555-204-7316
      </li>
      <li>
        <svg viewBox="0 0 24 24"><path d="M2 5h20v14H2z M2 5l10 8 10-8" fill="none" stroke="var(--navy)" stroke-width="3"/></svg>
        info@kelvorplant.com
      </li>
      <li>
        <svg viewBox="0 0 24 24"><circle cx="12" cy="12" r="10"/></svg>
        www.kelvorplant.com
      </li>
    </ul>

    <div class="brand">
      <span class="brand__dot" aria-hidden="true"></span>
      <span class="brand__name">Kelvor Plant Services</span>
    </div>

    <div class="divider" aria-hidden="true"></div>

    <address class="address">
      P.O. Box 418 Harlow Road<br>
      Dunmere Vale KT, K7R 2L9
    </address>
  </section>

  <section class="card card--back" aria-label="Business card back">
    <div class="brand">
      <span class="brand__dot" aria-hidden="true"></span>
      <span class="brand__name">Kelvor Plant Services</span>
    </div>
  </section>
</body>
</html>
```